Leaves In Motion (Podcast Artwork)

We require a podcast cover artwork, to stand out but also make our direction clear. This is a podcast about how everyone can make effective change to help the environment and limit the climate crisis.

The artwork needs to be 3000x3000 pixels for submission to Brindlecast Audio.

We would ideally like a planet image in there, perhaps within one of the 'o's. However, we are open to suggestions and alternative design options.

The use of green in the artwork would also be good.

```html
<!DOCTYPE html>
<html lang="en">
<head>
<meta charset="utf-8">
<title>Leaves In Motion – Podcast Artwork</title>
<link rel="stylesheet" href="https://fonts.googleapis.com/css2?family=Poppins:wght@800&family=Montserrat:wght@700&display=swap">
<style>
  :root {
    --green-bright: #5ba51b;
    --green-deep: #1d440a;
    --green-field: #5cb12c;
    --green-hill: #3c9418;
    --green-forest: #1e5c0a;
    --green-moss: #2d7214;
    --green-tree: #3f8c22;
    --green-pill: #1f4a0c;
    --white: #ffffff;
    --ink: #0b0b0b;
  }
  * { margin: 0; padding: 0; box-sizing: border-box; }
  html, body {
    width: 1200px;
    height: 1200px;
    overflow: hidden;
    background: var(--green-field);
  }
  .cover {
    position: relative;
    width: 1200px;
    height: 1200px;
    overflow: hidden;
  }
  .cover-art {
    position: absolute;
    inset: 0;
    width: 1200px;
    height: 1200px;
  }
  .title {
    position: absolute;
    top: 40px;
    left: 0;
    width: 1200px;
    text-align: center;
    font-family: 'Poppins', sans-serif;
    font-weight: 800;
    font-size: 180px;
    line-height: 175px;
    letter-spacing: -5px;
    color: var(--white);
    text-shadow: 5px 5px 0 var(--ink), 6px 7px 6px rgba(0,0,0,.45);
  }
  .title-line { display: block; }
  .badge {
    position: absolute;
    left: 421px;
    top: 492px;
    width: 349px;
    height: 87px;
    border-radius: 44px;
    background: var(--green-pill);
    color: var(--white);
    font-family: 'Montserrat', sans-serif;
    font-weight: 700;
    font-size: 62px;
    line-height: 87px;
    text-align: center;
    letter-spacing: 1px;
  }
</style>
</head>
<body>
<main class="cover">
  <svg class="cover-art" viewBox="0 0 1200 1200" xmlns="http://www.w3.org/2000/svg">
    <defs>
      <radialGradient id="header-glow" cx="0.5" cy="0.45" r="0.65">
        <stop offset="0" stop-color="var(--green-bright)"/>
        <stop offset="0.6" stop-color="#3a7a14"/>
        <stop offset="1" stop-color="var(--green-deep)"/>
      </radialGradient>
      <linearGradient id="photo-tones" x1="0" y1="0" x2="0" y2="1">
        <stop offset="0" stop-color="#c9a48e"/>
        <stop offset="0.35" stop-color="#6f8f3c"/>
        <stop offset="0.7" stop-color="#d9b3a0"/>
        <stop offset="1" stop-color="#3a2718"/>
      </linearGradient>
    </defs>

    <rect class="field" width="1200" height="1200" fill="var(--green-field)"/>

    <path class="header-band" d="M0 0 H1200 V333 Q600 520 0 344 Z" fill="url(#header-glow)"/>

    <path class="hill-left" d="M0 741 Q250 640 541 616 L559 690 L400 1200 L0 1200 Z" fill="var(--green-hill)"/>

    <ellipse class="tree-illustration" role="img" aria-label="Illustration of a small tree with scattered leaves"
             cx="1050" cy="690" rx="135" ry="160" fill="var(--green-tree)"/>

    <path class="band-left" d="M0 865 Q90 845 187 840 Q215 960 209 1083 L267 1076 L267 1200 L0 1200 Z" fill="var(--green-forest)"/>
    <path class="band-right" d="M1036 843 Q1120 845 1200 865 L1200 1200 L927 1200 L927 1040 L1018 1054 Q1015 950 1036 843 Z" fill="var(--green-moss)"/>

    <path class="photo-frame" d="M267 1200 V1018 A330 330 0 0 1 927 1018 V1200 Z" fill="#101010"/>
    <path class="photo" role="img" aria-label="Photo of two hands planting a young seedling in dark soil"
          d="M267 1200 V1018 A330 330 0 0 1 927 1018 V1200 Z" fill="url(#photo-tones)"/>
    <path class="photo-outline" d="M279 1200 V1018 A318 318 0 0 1 915 1018 V1200" fill="none" stroke="var(--white)" stroke-width="2.5"/>
  </svg>

  <h1 class="title">
    <span class="title-line">Leaves In</span>
    <span class="title-line">Motion</span>
  </h1>

  <div class="badge">Podcast</div>
</main>
</body>
</html>
```